The graphic design project is to create a book cover and potentially an accompanying logo for a book called The Steady Compass: A Field Guide for Guiding Teams Through Shifting Ground. The title is a working title and may change slightly. The book presents 10 capabilities that organizational leaders should have to be able to lead in a world filled with uncertainties. The main themes are the following:• Leaders need to be clear and focused about the overall mission, but also need to make strategic decisions with a diversity of opinions and options.• Leaders must anticipate where they will need to adapt in implementing strategy.• Leaders need to create a culture that promotes trust and agility.• Leaders need to be vigilant and look for early indicators of change. Show intellectual curiosity.• Leaders should be willing to experiment and learn from the experiments.The book is designed as a handbook. This will be a self published business book.The below graphic provides what are the key concepts representing each letter of “COMPASSING”. The right-hand column provides key words / phrases associated with the concepts.

Target Market(s)

Mid to Senior level executives at global companies across industries.

Colors

Designer to choose colors to be used in the design.

Requirements
Must have
• No must haves.
Nice to have
• Wide open on the design.

```html
<!DOCTYPE html>
<html lang="en">
<head>
<meta charset="utf-8">
<title>The Steady Compass — Book Cover</title>
<link href="https://fonts.googleapis.com/css2?family=Barlow+Condensed:wght@200;400&family=Barlow+Semi+Condensed:wght@300&family=Oswald:wght@700&display=swap" rel="stylesheet">
<style>
  :root {
    --page-bg: #e6e7e8;
    --cover-paper: #ebebeb;
    --brand-red: #c00f1c;
    --concept-gray: #b4b4b4;
    --subtitle-ink: #ffffff;
    --author-ink: #ffffff;
  }
  * { margin: 0; padding: 0; box-sizing: border-box; }
  html, body {
    width: 1200px; height: 1200px; overflow: hidden;
    background: var(--page-bg);
  }
  .stage { position: relative; width: 1200px; height: 1200px; }
  .cover {
    position: absolute; left: 220px; top: 137px;
    width: 952px; height: 1175px;
    transform: scale(0.8); transform-origin: 0 0;
    background: var(--cover-paper);
    overflow: hidden;
  }
  .cover-art { position: absolute; inset: 0; width: 952px; height: 1175px; }

  .spine-text {
    position: absolute; white-space: nowrap;
    transform: translate(-50%, -50%) rotate(-95.7deg);
  }
  .author-line {
    left: 113px; top: 611px;
    font: 400 40px/1 "Barlow Condensed", sans-serif;
    color: var(--author-ink);
  }
  .subtitle-line {
    left: 191px; top: 604px;
    font: 300 31px/1 "Barlow Semi Condensed", sans-serif;
    color: var(--subtitle-ink);
  }

  .title-letter {
    position: absolute;
    font: 700 49px/1 "Oswald", sans-serif;
    color: var(--brand-red);
  }
  .concept-line {
    position: absolute; white-space: nowrap;
    transform: rotate(-5.8deg); transform-origin: 0 100%;
    font: 200 52px/1 "Barlow Condensed", sans-serif;
    color: var(--concept-gray);
  }
  .concept-line .initial {
    font: 700 49px/1 "Oswald", sans-serif;
    color: var(--brand-red);
    margin-right: 2px;
  }
</style>
</head>
<body>
<div class="stage">
  <div class="cover">
    <svg class="cover-art" viewBox="0 0 952 1175" aria-hidden="true">
      <defs>
        <linearGradient id="stripeShade" x1="0" y1="0" x2="1" y2="0">
          <stop offset="0" stop-color="#9e9e9e"/>
          <stop offset="0.5" stop-color="#b4b4b4"/>
          <stop offset="1" stop-color="#c2c2c2"/>
        </linearGradient>
        <linearGradient id="paperShade" x1="0" y1="0" x2="1" y2="0">
          <stop offset="0" stop-color="#cfcfcf"/>
          <stop offset="1" stop-color="#ebebeb" stop-opacity="0"/>
        </linearGradient>
      </defs>
      <polygon points="165,0 310,0 430,1175 282,1175" fill="url(#paperShade)"/>
      <polygon points="93,0 165,0 282,1175 211,1175" fill="url(#stripeShade)"/>
      <polygon points="0,0 93,0 211,1175 0,1175" fill="var(--brand-red)"/>
    </svg>

    <div class="spine-text author-line">Autor Name &amp; Other Autor Name</div>
    <div class="spine-text subtitle-line">A Field Guide for Guiding Teams Through Shifting Ground</div>

    <h1 aria-label="The Compassing Leader — The Steady Compass">
      <span class="title-letter" style="left:255px;top:128px">T</span>
      <span class="title-letter" style="left:260px;top:177px">H</span>
      <span class="title-letter" style="left:265px;top:224px">E</span>

      <span class="concept-line" style="left:272px;top:300px"><span class="initial">C</span>OMMON PURPOSE</span>
      <span class="concept-line" style="left:277px;top:348px"><span class="initial">O</span>PEN EXPERIENCE FRAMES</span>
      <span class="concept-line" style="left:282px;top:395px"><span class="initial">M</span>ANY OPTIONS</span>
      <span class="concept-line" style="left:287px;top:443px"><span class="initial">P</span>USHBACK WELCOMED</span>
      <span class="concept-line" style="left:292px;top:490px"><span class="initial">A</span>NTICIPATED FUTURE FORCES</span>
      <span class="concept-line" style="left:297px;top:538px"><span class="initial">S</span>ENSIBLE PARANOIA</span>
      <span class="concept-line" style="left:302px;top:585px"><span class="initial">S</span>HARED TRUST</span>
      <span class="concept-line" style="left:307px;top:633px"><span class="initial">I</span>NTERNAL CONDITIONS</span>
      <span class="concept-line" style="left:312px;top:680px"><span class="initial">N</span>OTICING EARLY SIGNALS</span>
      <span class="concept-line" style="left:317px;top:728px"><span class="initial">G</span>ROWTH BY EXPERIMENT</span>

      <span class="title-letter" style="left:323px;top:803px">L</span>
      <span class="title-letter" style="left:328px;top:851px">E</span>
      <span class="title-letter" style="left:333px;top:899px">A</span>
      <span class="title-letter" style="left:338px;top:946px">D</span>
      <span class="title-letter" style="left:343px;top:994px">E</span>
      <span class="title-letter" style="left:348px;top:1042px">R</span>
    </h1>
  </div>
</div>
</body>
</html>
```